Australian Skilled Migration

We need to design a add/flyer for a newspaper/magazine to promote our Australian Migration firm services. We targeting overseas graduating students and professionals who would like to Permanently Migrate to Australia.

We would like to advertise following services to our potential clients:

AUSTRALIA NEEDS YOU!!!

# Are you young and energetic individual?
# Do you have qualifications, work experiences or both?
# Perhaps you would like to open a small business, and sponsor yourself to live in Australia?
# Aspiring for job security and the highest living standards?

Contact us to find out how we can help you with Permanent Migration to Australia.

First consultation and eligibility assessment is free ! Tell your friends about us and receive a discount on your future fees!!

For more information please visit our website: www.corvintrak.org.au

(for a background we would like to use Australian themes such as: sandy beaches, ect... light colours)

Target Market(s)

Students
University graduates
Trade people with qualifications
Industry professionals
Anyone who wants to migrate to Australia

Industry/Entity Type

Security

Requirements
Must have
• our logo and website
easy to see and read the txt

Catchy Background
Nice to have
• as per our requirements
(designer questions, please e-mail: info@corvintrak.org. au)

```html
<!DOCTYPE html>
<html lang="en">
<head>
<meta charset="utf-8">
<title>Australia Needs You – Halden &amp; Co</title>
<link href="https://fonts.googleapis.com/css2?family=Lato:wght@400;700;900&display=swap" rel="stylesheet">
<style>
  :root {
    --red: #e41e26;
    --white: #ffffff;
    --yellow: #f9dc1c;
    --navy: #0f1a3c;
    --navy-deep: #0b1433;
    --sky-top: #3a5fa8;
    --sky-mid: #7d6a9e;
    --dusk: #e0743a;
    --water: #1a2a5c;
  }
  * { margin: 0; padding: 0; box-sizing: border-box; }
  html, body { width: 849px; height: 1200px; overflow: hidden; background: var(--navy); }
  .flyer {
    position: relative;
    width: 849px;
    height: 1200px;
    overflow: hidden;
    font-family: 'Lato', Arial, sans-serif;
    background: var(--navy);
    color: var(--white);
  }
  .harbour-scene {
    position: absolute;
    left: 0; top: 0;
    width: 849px; height: 880px;
    background: linear-gradient(180deg,
      var(--sky-top) 0%,
      #5a6fb0 18%,
      var(--sky-mid) 34%,
      #c0607a 44%,
      var(--dusk) 52%,
      #c9892f 57%,
      var(--water) 64%,
      #14224f 80%,
      var(--navy) 100%);
  }
  .headline {
    position: absolute;
    left: 64px; top: 60px;
    width: 727px; height: 243px;
    background: var(--red);
    box-shadow: 10px 10px 0 rgba(20, 20, 40, 0.75);
    display: flex; flex-direction: column; align-items: center; justify-content: center;
  }
  .headline::before {
    content: "";
    position: absolute;
    inset: 7px;
    border: 3px solid var(--white);
  }
  .headline span {
    display: block;
    font-weight: 900;
    font-size: 108px;
    line-height: 96px;
    color: var(--white);
    letter-spacing: 1px;
  }
  .questions {
    position: absolute;
    left: 0; top: 562px;
    width: 849px;
    text-align: center;
    font-weight: 700;
  }
  .q-young { font-size: 35px; color: var(--white); line-height: 42px; }
  .q-qualified { font-size: 36px; color: var(--yellow); line-height: 45px; margin-top: 10px; }
  .q-business { font-size: 26px; color: var(--white); line-height: 33px; margin-top: 6px; }
  .q-security { font-size: 27px; color: var(--yellow); line-height: 34px; margin-top: 18px; }
  .contact-panel {
    position: absolute;
    left: 0; top: 868px;
    width: 849px; height: 272px;
    background: var(--navy-deep);
  }
  .contact-title {
    position: absolute;
    left: 0; top: 852px;
    width: 849px;
    text-align: center;
    font-weight: 700;
    font-size: 52px;
    line-height: 60px;
    color: var(--yellow);
  }
  .contact-copy {
    position: absolute;
    left: 56px; top: 925px;
    font-size: 19.5px;
    line-height: 29px;
    color: var(--white);
  }
  .more-info {
    position: absolute;
    left: 56px; top: 1040px;
    font-size: 19.5px;
    color: var(--white);
  }
  .website {
    position: absolute;
    left: 56px; top: 1070px;
    font-size: 36px;
    font-weight: 700;
    color: var(--yellow);
  }
  .brand {
    position: absolute;
    left: 562px; top: 1040px;
    display: flex; align-items: center; gap: 10px;
  }
  .brand-mark {
    width: 44px; height: 44px;
    border-radius: 50%;
    background: var(--red);
  }
  .brand-name {
    font-weight: 700;
    font-size: 26px;
    color: var(--red);
  }
  .footer-band {
    position: absolute;
    left: 0; top: 1140px;
    width: 849px; height: 60px;
    background: var(--red);
  }
</style>
</head>
<body>
<main class="flyer">
  <div class="harbour-scene" role="img" aria-label="Sydney Opera House and Harbour Bridge lit up at sunset under a blue and orange sky over the harbour"></div>

  <h1 class="headline"><span>AUSTRALIA</span><span>NEEDS YOU!!!</span></h1>

  <section class="questions">
    <p class="q-young">Are you young and energetic individual?</p>
    <p class="q-qualified">Do you have qualifications, work<br>experiences or both?</p>
    <p class="q-business">Perhaps you would like to open a small business<br>and sponsor yourself to live in Australia?</p>
    <p class="q-security">Aspiring for job security and the highest living standards?</p>
  </section>

  <div class="contact-panel"></div>
  <h2 class="contact-title">Contact us</h2>
  <p class="contact-copy">
    To find out how we can help you with Permanent Migration to Australia.<br>
    First consultation and eligibility assessment is free !<br>
    Tell your friends about us and receive a discount on your future fees!!
  </p>
  <p class="more-info">For more information please visit our website:</p>
  <p class="website">www.corvintrak.org.au</p>

  <div class="brand">
    <span class="brand-mark"></span>
    <span class="brand-name">Halden &amp; Co</span>
  </div>

  <div class="footer-band"></div>
</main>
</body>
</html>
```